Health and Fitness Club requires a stunning and simple website

We are a health and fitness club based in Dubai, when we launch we will be the biggest club in the country, we will also have the 2 largest activity rooms in the country, we are setting a new standard in the industry by offering one thing, our attitude.

Our attitude means the following:
unlike other clubs we have no hidden charges or fees
our members can join daily, monthly, 6 months or annually
our service and facility are comparable to 5* hotel gyms
our equipment is second to none
our space is the biggest in the country
we do not force our members to use our in-house personal trainers - you can bring your own and we will not charge them entry!
we will have a cutting edge crossfit box in our gym with classes by the best trainers in the country
we will be providing free-lance personal trainers a platform to engage customers, grow their business and even use our activity rooms for classes

Basically we will be a gym like no other, simply because we are gym people and we hate the restrictive practices and hidden charges by other gyms, so we are making our own gym which focuses on quality and service.

All of this has to be communicated in the style of the website, the colors of the website we want to be limited to the logo colors as this will be the same theme running throughout the gym.

The landing page of the website HAS to incorporate elements from our social media presences, this basically is the usual, twitter, instagram, facebook. We can have these as a sidebar, the centre of the page should display the latest article from our blog (also on the website) Also we need to have a calendar for activities and classes on the front page. The menu should have links to the following:
Latest News
About us
Team
Gallery
Membership
Classes
Member Log In
Contact Us
Location

The style of the website has to be similar to the logo, particularly in terms of the fonts used.

Fitness

```html
<!DOCTYPE html>
<html lang="en">
<head>
<meta charset="utf-8">
<title>Ironhouse Fitness Club</title>
<link rel="stylesheet" href="https://fonts.googleapis.com/css2?family=Ubuntu:wght@400;500&family=Open+Sans:ital,wght@0,400;1,400&display=swap">
<style>
:root{
  --red:#b30812;
  --red-dark:#9a0610;
  --red-nav:#c10a14;
  --white:#ffffff;
  --ink:#555555;
  --muted:#888888;
  --line:#dddddd;
  --footer:#4a4a4a;
  --cal-head:#3a3a3a;
  --blue:#1a5ed8;
}
*{box-sizing:border-box;margin:0;padding:0}
html,body{width:943px;height:1200px;overflow:hidden;background:var(--white)}
body{font-family:"Open Sans",Arial,sans-serif;color:var(--ink);position:relative}
.page{position:relative;width:943px;height:1200px}
.abs{position:absolute}

.brand{left:71px;top:30px;display:flex;align-items:center;gap:10px;font-family:"Ubuntu",sans-serif;font-weight:500;font-size:26px;color:var(--red);height:66px}
.brand-dot{width:22px;height:22px;border-radius:50%;background:var(--red)}
.search{left:670px;top:58px;width:205px;height:28px;border:1px solid #cfcfcf;font-size:12px;color:#888;padding:6px 10px;display:flex;justify-content:space-between;align-items:center}

.nav{left:0;top:127px;width:943px;height:36px;background:linear-gradient(var(--red-nav),var(--red-dark));display:flex;padding-left:67px}
.nav a{font-family:"Ubuntu",sans-serif;font-size:13.5px;color:var(--white);text-decoration:none;line-height:36px;padding:0 17px;border-right:1px solid rgba(0,0,0,.18)}
.nav a:first-child{background:rgba(0,0,0,.1)}
.nav a:last-child{border-right:none}

.hero{left:0;top:163px;width:943px;height:436px;background:linear-gradient(100deg,#6fa8c8 0%,#c9dde8 35%,#eef3f5 60%,#a9c9da 100%)}
.caption{left:173px;top:327px;width:389px;height:118px;background:rgba(110,110,110,.72);color:var(--white);padding:16px 22px}
.caption h1{font-family:"Ubuntu",sans-serif;font-weight:400;font-size:29px;margin-bottom:8px}
.caption p{font-size:13.5px;line-height:22px}
.arrow{width:48px;height:48px;border-radius:50%;background:rgba(110,110,110,.8);top:356px;display:flex;align-items:center;justify-content:center}

.card{top:534px;width:251px;height:210px;background:linear-gradient(135deg,var(--red) 55%,var(--red-dark) 55%);color:var(--white);padding:22px 22px}
.card h2{font-family:"Ubuntu",sans-serif;font-weight:500;font-size:21px}
.card .sub{font-family:"Ubuntu",sans-serif;font-size:14px;margin-top:6px}
.schedule{margin-top:20px;font-size:12px;list-style:none}
.schedule li{display:flex;align-items:center;height:28px}
.schedule svg{margin-right:9px}
.schedule .time{margin-left:auto}
.offer{display:flex;margin-top:20px;gap:22px;font-size:11.5px;line-height:17px}
.offer .icon{width:47px;height:47px;flex:none;border-radius:50%;background:var(--white);display:flex;align-items:center;justify-content:center;margin-top:8px}
.more{position:absolute;right:32px;bottom:16px;font-size:12px}

.section-title{left:67px;top:793px;font-family:"Ubuntu",sans-serif;font-size:18px;color:var(--red)}
.article{left:67px;width:500px;display:flex;gap:17px}
.thumb{width:106px;height:98px;border:1px solid var(--line);padding:3px;flex:none}
.thumb div{width:100%;height:100%}
.article h3{font-family:"Ubuntu",sans-serif;font-weight:400;font-size:13.5px;color:var(--red);margin-bottom:6px}
.article p{font-size:10.5px;line-height:17px;color:#777}
.meta{display:flex;align-items:center;gap:16px;margin-top:6px;font-size:9.5px;font-style:italic;color:#555}
.btn{font-style:normal;font-size:10px;border:1px solid #ccc;border-radius:3px;padding:1px 7px;background:#f3f3f3;color:#335}

.calendar{left:602px;top:794px;width:272px;border:1px solid #ccc;box-shadow:0 1px 3px rgba(0,0,0,.15)}
.cal-head{height:42px;background:var(--cal-head);color:var(--white);display:flex;align-items:center;justify-content:space-between;padding:0 14px;font-family:"Ubuntu",sans-serif;font-size:15px}
.cal-grid{display:grid;grid-template-columns:repeat(7,1fr)}
.dname{height:22px;font-size:9px;color:#666;text-align:center;line-height:22px;border-bottom:1px solid #e3e3e3}
.day{height:38.5px;border-right:1px solid #e5e5e5;border-bottom:1px solid #e5e5e5;font-size:11px;font-weight:bold;color:#333;display:flex;align-items:center;justify-content:center;position:relative;background:linear-gradient(#fff,#f1f1f1)}
.day.off{color:#aaa;font-weight:normal}
.day.event::after{content:"";position:absolute;bottom:7px;left:50%;width:3px;height:3px;margin-left:-1.5px;border-radius:50%;background:#555}
.day.today{background:var(--blue);color:var(--white);border:2px solid #0a3ea8}
.day.today::after{background:var(--white)}

.footer{left:0;top:1106px;width:943px;height:94px;background:var(--footer);color:var(--white);font-family:Arial,sans-serif;font-size:11.5px}
.footer .links{position:absolute;left:69px;top:31px}
.footer .copy{position:absolute;left:69px;top:59px}
.socials{position:absolute;left:715px;top:35px;display:flex;gap:11px}
.socials span{width:28px;height:28px;display:block}
</style>
</head>
<body>
<div class="page">
  <div class="abs brand"><span class="brand-dot"></span>Ironhouse</div>
  <div class="abs search">Search..
    <svg width="11" height="11" viewBox="0 0 11 11"><circle cx="4.5" cy="4.5" r="3.5" fill="none" stroke="#999" stroke-width="1.5"/><line x1="7" y1="7" x2="10" y2="10" stroke="#999" stroke-width="1.5"/></svg>
  </div>

  <nav class="abs nav">
    <a href="#">Home</a><a href="#">About us</a><a href="#">Team</a><a href="#">Gallery</a><a href="#">Membership</a><a href="#">Classes</a><a href="#">Member Log In</a><a href="#">Contact Us</a><a href="#">Location</a>
  </nav>

  <div class="abs hero" role="img" aria-label="Photo of a smiling man and woman training on cardio machines in a bright gym"></div>
  <div class="abs caption">
    <h1>Gym Fitness amd Training</h1>
    <p>Anim pariatur cliche reprehenderit, enim eiusmod high life accusamus marlow penfield ad squid</p>
  </div>
  <div class="abs arrow" style="left:68px"><svg width="14" height="22" viewBox="0 0 14 22"><polyline points="11,2 3,11 11,20" fill="none" stroke="#fff" stroke-width="2"/></svg></div>
  <div class="abs arrow" style="left:826px"><svg width="14" height="22" viewBox="0 0 14 22"><polyline points="3,2 11,11 3,20" fill="none" stroke="#fff" stroke-width="2"/></svg></div>

  <div class="abs card" style="left:69px">
    <h2>What's Next</h2>
    <div class="sub">Upcoming Classes</div>
    <ul class="schedule">
      <li><svg width="12" height="12" viewBox="0 0 12 12"><circle cx="6" cy="6" r="5" fill="none" stroke="#fff" stroke-width="1.2"/><polyline points="6,3 6,6 8.5,6" fill="none" stroke="#fff" stroke-width="1.2"/></svg>Gym Fitness<span class="time">12.00 - 13.00</span></li>
      <li><svg width="12" height="12" viewBox="0 0 12 12"><circle cx="6" cy="6" r="5" fill="none" stroke="#fff" stroke-width="1.2"/><polyline points="6,3 6,6 8.5,6" fill="none" stroke="#fff" stroke-width="1.2"/></svg>Boxing<span class="time">12.00 - 13.00</span></li>
      <li><svg width="12" height="12" viewBox="0 0 12 12"><circle cx="6" cy="6" r="5" fill="none" stroke="#fff" stroke-width="1.2"/><polyline points="6,3 6,6 8.5,6" fill="none" stroke="#fff" stroke-width="1.2"/></svg>Yoga pilates<span class="time">12.00 - 13.00</span></li>
    </ul>
  </div>

  <div class="abs card" style="left:346px">
    <h2>Membership Cards</h2>
    <div class="sub">25% discount for all members</div>
    <div class="offer">
      <div class="icon"><svg width="16" height="14" viewBox="0 0 16 14"><rect x="1" y="3" width="14" height="10" fill="#222"/><rect x="5" y="1" width="6" height="3" fill="#222"/><rect x="4" y="6" width="8" height="1.5" fill="#fff"/><rect x="4" y="9" width="8" height="1.5" fill="#fff"/></svg></div>
      <div>Discount on services and treatments at the FitHall for all membership cards holders.</div>
    </div>
    <span class="more">More..</span>
  </div>

  <div class="abs card" style="left:624px">
    <h2>Classes</h2>
    <div class="sub">Signup Today</div>
    <div class="offer">
      <div class="icon"><svg width="15" height="15" viewBox="0 0 15 15"><rect x="1" y="2" width="13" height="12" fill="#222"/><g fill="#fff"><rect x="3" y="5" width="2" height="2"/><rect x="6.5" y="5" width="2" height="2"/><rect x="10" y="5" width="2" height="2"/><rect x="3" y="8.5" width="2" height="2"/><rect x="6.5" y="8.5" width="2" height="2"/><rect x="10" y="8.5" width="2" height="2"/></g></svg></div>
      <div>Discount on services and treatments at the FitHall for all membership cards holders.</div>
    </div>
    <span class="more">More..</span>
  </div>

  <h2 class="abs section-title">Latest Articles</h2>

  <article class="abs article" style="top:836px">
    <div class="thumb"><div role="img" aria-label="Photo of a muscular athlete lifting weights" style="background:linear-gradient(135deg,#c98f6a,#7a8f9a)"></div></div>
    <div>
      <h3>Suspendisse eu erat quam. Vivamus porttitor eros quis.</h3>
      <p>Suspendisse eu erat quam. Vivamus porttitor eros quis nisi lacinia sed interdum uam a orci quis nisi sagittis sagittis. Etiam adipiscing, justo quis feugiat.Suspend amus porttitor eros quis nisi lacinia sed interdum lorem vulputate.</p>
      <div class="meta">Posted on 02 June, 2013 <span class="btn">Follow</span><span class="btn">Like</span></div>
    </div>
  </article>

  <article class="abs article" style="top:959px">
    <div class="thumb"><div role="img" aria-label="Photo of people riding exercise bikes in a class" style="background:linear-gradient(135deg,#e8e4e0,#7c9bb0)"></div></div>
    <div>
      <h3>Suspendisse eu erat quam. Vivamus porttitor eros quis.</h3>
      <p>Suspendisse eu erat quam. Vivamus porttitor eros quis nisi lacinia sed interdum uam a orci quis nisi sagittis sagittis. Etiam adipiscing, justo quis feugiat.Suspend amus porttitor eros quis nisi lacinia sed interdum lorem vulputate.</p>
      <div class="meta">Posted on 02 June, 2013 <span class="btn">Follow</span><span class="btn">Like</span></div>
    </div>
  </article>

  <div class="abs calendar">
    <div class="cal-head">
      <svg width="8" height="12" viewBox="0 0 8 12"><polyline points="7,1 2,6 7,11" fill="none" stroke="#fff" stroke-width="2"/></svg>
      January 2012
      <svg width="8" height="12" viewBox="0 0 8 12"><polyline points="1,1 6,6 1,11" fill="none" stroke="#fff" stroke-width="2"/></svg>
    </div>
    <div class="cal-grid">
      <div class="dname">MON</div><div class="dname">TUE</div><div class="dname">WED</div><div class="dname">THU</div><div class="dname">FRI</div><div class="dname">SAT</div><div class="dname">SUN</div>
      <div class="day off event">30</div><div class="day">1</div><div class="day event">2</div><div class="day">3</div><div class="day">4</div><div class="day">5</div><div class="day">6</div>
      <div class="day">7</div><div class="day">8</div><div class="day">9</div><div class="day">10</div><div class="day">11</div><div class="day today event">12</div><div class="day">13</div>
      <div class="day">14</div><div class="day">15</div><div class="day event">16</div><div class="day event">17</div><div class="day">18</div><div class="day">19</div><div class="day">20</div>
      <div class="day event">21</div><div class="day">22</div><div class="day">23</div><div class="day">24</div><div class="day">25</div><div class="day">26</div><div class="day">27</div>
      <div class="day">28</div><div class="day">29</div><div class="day">30</div><div class="day">31</div><div class="day off">1</div><div class="day off">2</div><div class="day off">3</div>
    </div>
  </div>

  <footer class="abs footer">
    <div class="links">Terms and Conditions | Privacy Policy | Site Map</div>
    <div class="copy">Copyright © 2013. All Rights Reserved.</div>
    <div class="socials">
      <span style="background:#3b5ba0" aria-label="Social link"></span>
      <span style="background:#2aa3dc" aria-label="Social link"></span>
      <span style="background:#f26c1a" aria-label="Social link"></span>
      <span style="background:#d8232a" aria-label="Social link"></span>
    </div>
  </footer>
</div>
</body>
</html>
```